International Educational/Tuition/Learning Center

Company Background:
- Business card for a educational/tuition/learning center that provides supplementary lessons for students in Grade 7 to 12 ( Secondary and JC syllabus in the GCE 'O' and GCE 'A' level context but not limited to these. Future plans will be to cater for SAT, IB and HSCs programs.
- Name of company is called "THE QUILL AND LANTERN".
- Vision is to complement the basic principles of the rote learning culture and value-add by training the students to think out of the box and preserve creativity.
- To re-define and retain the value of the learning process.

Sketch Design:
- Simple and classy design that is mainly white-based with tinge of refreshing bright lime green.
- "New Age" simple and classy design that appeals to teenagers and young adults.
- Logo design to reinforce the vision of company.

Rough idea of what we have in mind but pls do not let this restrict your creativity:
- White and bright green base
- 2 sided print
- Front with simple information of Name and Designation as well as de-bossed/letterpressed print
- Details of on reverse side
- Contact details can be categorized as " find me" - address, "call me" - contact number , "email me" - email address, " Find out more"- website.

Information:

Name: Darel K Thuam
Title: Managing Director
Address: 41 Pelham Crescent, #07-15, Singapore 654321
Contact: +65 91234056
Email: darelthuam@mailvesta.com
Website: www.qnl-tutor.com

Thank you all in advance! Looking forward to some amazing designs from all you talented folks!
Updates

hi all,

have updated the projected to a guranteed status from the initial refundable status.

Thanks 

Dear designers,

I've included more info into the brief on design elements to include. 

Thanks for your participation and efforts!

Cheers!

Target Market(s)

young parents with school going children

Industry/Entity Type

Training

Requirements
Must have
• debossed/letterpressed logo
feel free to be creative with ur designs!
Nice to have
• round edges
Logo/name could have some elements of education/knowledge/path-to-learning incorporated in the design concept

```html
<!DOCTYPE html>
<html lang="en">
<head>
<meta charset="utf-8">
<title>The Quill and Lantern – Business Card</title>
<link rel="stylesheet" href="https://fonts.googleapis.com/css2?family=Righteous&family=Open+Sans:wght@300;400&display=swap">
<style>
  :root {
    --backdrop: #d9d9d9;
    --card-white: #ffffff;
    --lime: #a6f000;
    --lime-deep: #8fd400;
    --lime-light: #b4ff14;
    --ink: #111111;
    --ink-soft: #333333;
  }
  * { margin: 0; padding: 0; box-sizing: border-box; }
  html, body {
    width: 1200px;
    height: 900px;
    overflow: hidden;
  }
  body {
    position: relative;
    background: var(--backdrop);
    font-family: "Open Sans", sans-serif;
  }
  .card {
    position: absolute;
    width: 560px;
    height: 330px;
    background: var(--card-white);
    overflow: hidden;
    box-shadow: 0 4px 14px rgba(0, 0, 0, 0.18);
  }
  .card--front { left: 580px; top: 100px; }
  .card--back  { left: 120px; top: 470px; }

  .holder-name {
    font-family: "Righteous", sans-serif;
    font-size: 40px;
    line-height: 1;
    letter-spacing: 0.5px;
  }
  .holder-title {
    font-family: "Righteous", sans-serif;
    font-size: 17px;
    line-height: 1;
    letter-spacing: 0.5px;
  }

  /* Front side */
  .front-identity {
    position: absolute;
    left: 0;
    right: 0;
    top: 82px;
    text-align: center;
    color: var(--lime);
  }
  .front-identity .holder-title {
    display: block;
    margin-top: 2px;
    padding-left: 40px;
  }
  .company-name {
    position: absolute;
    left: 0;
    right: 0;
    top: 176px;
    text-align: center;
    font-weight: 300;
    font-size: 28px;
    letter-spacing: 0.5px;
    color: var(--lime);
  }
  .front-band {
    position: absolute;
    left: 0;
    right: 0;
    bottom: 0;
    height: 60px;
    background: linear-gradient(to bottom, var(--lime-light), var(--lime-deep));
  }

  /* Back side */
  .back-stripe {
    position: absolute;
    top: 0;
    right: 0;
    width: 48px;
    height: 100%;
    background: linear-gradient(to bottom, var(--lime-light), var(--lime-deep));
  }
  .back-identity {
    position: absolute;
    left: 40px;
    top: 92px;
    color: var(--ink);
  }
  .back-identity .holder-title {
    display: block;
    margin-top: 2px;
    padding-left: 6px;
  }
  .contact-list {
    position: absolute;
    left: 50px;
    top: 208px;
    list-style: none;
    font-size: 14px;
    line-height: 21px;
    color: var(--ink-soft);
    font-weight: 300;
    text-transform: uppercase;
  }
  .contact-list .label {
    font-weight: 400;
    color: var(--ink);
  }
</style>
</head>
<body>
  <section class="card card--front" aria-label="Business card, front">
    <div class="front-identity">
      <span class="holder-name">DAREL K THUAM</span>
      <span class="holder-title">MANAGING DIRECTOR</span>
    </div>
    <p class="company-name">THE QUILL AND LANTERN</p>
    <div class="front-band"></div>
  </section>

  <section class="card card--back" aria-label="Business card, back">
    <div class="back-identity">
      <span class="holder-name">DAREL K THUAM</span>
      <span class="holder-title">MANAGING DIRECTOR</span>
    </div>
    <ul class="contact-list">
      <li><span class="label">Address:</span> 41 Pelham Crescent, #07-15, Singapore 654321</li>
      <li><span class="label">Contact:</span> +65 91234056</li>
      <li><span class="label">Email:</span> darelthuam@mailvesta.com</li>
      <li><span class="label">Website:</span> www.qnl-tutor.com</li>
    </ul>
    <div class="back-stripe"></div>
  </section>
</body>
</html>
```